Corvane Transit Assoc needs Info graphic 1 pager (front & back)

We are looking for design work for an infographic type 1 pager (front and back). We will provide the information for the project. I need your help in the layout. Please see attachments for a general idea and direction. I value your design ideas, though, so please feel free to add your personal touch.

Front page is the new infographic that you are creating based off of my hand drafted sketch.

Back page is simply using the Flowchart from the Tellis Review Bureau.

Target Market(s)

State Legislators

Industry/Entity Type

Work

Requirements
Must have
• Nice looking info graphic one-pager. Please try to use the photos I sent in the graphic or similar rail clip art. Make the numbers stand out where possible. Give them emphasis.
• Make it clean. I want to share this info in short/quick meetings with legislators. I want it easy to decipher.
Nice to have
• Bold, strong colors.

```html
<!DOCTYPE html>
<html lang="en">
<head>
<meta charset="utf-8">
<title>Corvane Transit Assoc – Freight Railroad Funding One-Pager</title>
<link href="https://fonts.googleapis.com/css2?family=Oswald:wght@400;500;600;700&family=Roboto+Condensed:wght@400;700&display=swap" rel="stylesheet">
<style>
:root{
  --rust:#bf5a22;
  --orange:#ef8a1f;
  --orange-deep:#e0601c;
  --yellow:#f4c21f;
  --cyan:#1ea5d6;
  --steel:#8e9ea4;
  --blue:#2c4f98;
  --navy:#1d3470;
  --ink:#1b1b1b;
  --red:#c8251d;
  --flow:#1c7fb4;
  --paper:#ffffff;
  --bg:#ece9e4;
  --head:"Oswald",sans-serif;
  --body:"Roboto Condensed",sans-serif;
}
*{box-sizing:border-box;margin:0;padding:0}
html,body{width:1200px;height:1200px;overflow:hidden;background:var(--bg)}
.sheet{position:absolute;top:242px;width:586px;height:754px;transform:scale(.95);transform-origin:0 0;background:var(--paper);overflow:hidden;box-shadow:0 6px 18px rgba(0,0,0,.18)}
.front{left:33px}
.back{left:610px}
.abs{position:absolute}
.head{font-family:var(--head);font-weight:600;color:#fff;text-transform:uppercase;line-height:1}
.body{font-family:var(--body)}
.nocase{text-transform:none}

/* front */
.front-title{left:0;top:0;width:586px;height:117px;background:var(--rust);text-align:center;padding-top:14px;font-size:41px;line-height:1.05;letter-spacing:.5px;border-bottom:3px solid #fff}
.front-title span{display:block}
.ctf-block{left:0;top:117px;width:292px;height:318px;background:linear-gradient(180deg,#2f5fae 0%,#6f97c9 45%,#c9d6e6 70%,#9fb1c6 100%)}
.ctf-label{left:33px;top:125px;font-size:14px;font-weight:500;line-height:1.15}
.ctf-figure{left:33px;top:160px;font-size:34px}
.tag-freight{left:0;top:196px;width:218px;height:50px;background:var(--orange-deep);border-radius:0 10px 10px 0}
.tag-freight .pct{position:absolute;left:33px;top:4px;font-size:44px;color:#fff}
.tag-freight .lbl{position:absolute;left:136px;top:5px;font-size:19px;color:#fde9a8;text-align:center}
.tag-freight svg{position:absolute;left:104px;top:0}
.fed-strip{left:0;top:392px;width:292px;height:43px;background:var(--navy);color:#fff;font-size:14.5px;line-height:1.2;padding:3px 0 0 33px}
.stat{left:292px;width:294px;height:80px}
.stat .big{position:absolute;left:18px;font-size:36px;color:#fff}
.stat .txt{position:absolute;left:112px;color:#fff}
.stat svg{position:absolute;left:0;top:0}
.s1{top:117px;background:linear-gradient(90deg,var(--orange) 0%,var(--orange-deep) 100%)}
.s2{top:197px;background:var(--cyan)}
.s3{top:276px;background:var(--steel)}
.s4a{left:292px;top:355px;width:148px;height:80px;background:var(--yellow);text-align:center;color:var(--navy)}
.s4b{left:440px;top:355px;width:146px;height:80px;background:linear-gradient(90deg,var(--orange) 0%,var(--orange-deep) 100%);text-align:center}
.safety{left:0;top:435px;width:586px;height:227px;background:linear-gradient(180deg,var(--blue) 0%,#3b63ad 100%)}
.safety-tag{left:0;top:445px;width:180px;height:40px}
.safety-tag span{position:absolute;left:33px;top:2px;font-size:36px;color:#fff}
.crossing-art{left:45px;top:492px;width:95px;height:170px;border-radius:4px;background:linear-gradient(180deg,#e9e1d6 0%,#b7413a 55%,#3b3b3b 100%)}
.divider{top:470px;width:1px;height:150px;background:rgba(255,255,255,.4)}
.program{top:470px;width:185px;text-align:center;color:#fff}
.program .k1{font-size:16px;font-weight:500}
.program .k2{font-size:26px;font-weight:500;margin-top:1px}
.program .amt{font-size:38px;font-weight:600;margin-top:14px;text-transform:none}
.program p{font-family:var(--body);font-size:12.5px;line-height:1.25;text-align:justify;margin-top:14px;text-transform:none;font-weight:400}
.front-foot{left:0;top:662px;width:586px;height:92px;background:linear-gradient(90deg,#1a3068 0%,var(--navy) 100%)}
.assoc-name{left:103px;top:662px;width:102px;height:92px;background:#fff;display:flex;align-items:center;justify-content:center;text-align:center;font-family:var(--head);font-weight:500;font-size:15px;line-height:1.15;color:var(--navy);text-transform:uppercase}
.foot-line{left:218px;top:671px;color:#fff;font-size:22px;line-height:1.1;text-transform:none}

/* back */
.back-title{left:0;top:0;width:586px;height:83px;background:var(--rust);text-align:center;font-size:20px;font-weight:500;padding-top:31px;line-height:1.2;text-transform:none}
.flow{font-family:var(--body);color:var(--ink);font-size:12px;line-height:1.23;text-align:center}
.box{position:absolute;border:1px solid #b9b9b9;border-radius:6px;background:#fff}
.box b.h{display:block;color:var(--red);font-family:var(--body);font-weight:700}
.box b.hb{display:block;color:var(--navy);font-weight:700}
.mtf{left:63px;top:88px;width:459px;height:77px;border-color:var(--orange)}
.mtf b.h{font-family:var(--head);font-weight:500;font-size:17px;margin:3px 0 1px}
.blue-box{border:2px solid var(--flow);color:var(--flow)}
.grants{left:313px;top:170px;width:239px;height:157px;text-align:left;padding:1px 4px 0;font-size:11px;line-height:1.32}
.grants b.hb{text-align:center;font-size:12.5px;margin-bottom:8px}
.row{display:flex;justify-content:space-between}
.row .v{font-weight:700}
.sm{font-size:8px;line-height:1.2}
.county{left:178px;width:230px;height:66px;font-size:10px;line-height:1.22;padding-top:2px}
.county b.h{font-size:10px}
.back-foot{left:0;top:665px;width:586px;height:89px;background:linear-gradient(90deg,#1a3068 0%,var(--navy) 100%)}
.note{left:33px;top:672px;width:410px;color:#fff;font-family:var(--body);font-size:7px;line-height:1.25}
.bureau{left:450px;top:676px;width:110px;color:#fff;font-family:var(--head);font-weight:600;font-size:15px;line-height:1.05;text-transform:uppercase;text-align:center}
.byline{left:440px;top:713px;width:130px;color:#fff;font-family:var(--body);font-weight:700;font-size:7px;text-align:center}
</style>
</head>
<body>

<section class="sheet front">
  <h1 class="abs head front-title"><span>Public Act 51 of 1951</span><span>Freight Railroad Funding</span></h1>

  <div class="abs ctf-block" role="img" aria-label="Photo of a blue freight locomotive under a cloudy sky"></div>
  <div class="abs head ctf-label">Compvehensive Transporatian Fund<br>US to 10% of MTF Sec 10</div>
  <div class="abs head ctf-figure nocase">CTF $ 320,5m</div>
  <div class="abs tag-freight">
    <svg width="30" height="50" viewBox="0 0 30 50"><polygon points="0,0 12,0 30,25 12,50 0,50 18,25" fill="#f4c21f"/></svg>
    <span class="pct head">2%</span>
    <span class="lbl head">Freight<br>Rail</span>
  </div>
  <div class="abs body fed-strip">Freight Economic Development<br>Freight Property Management</div>

  <div class="abs stat s1">
    <svg width="294" height="80"><polygon points="90,0 112,0 104,80 82,80" fill="#f4c21f" opacity=".85"/></svg>
    <span class="big head" style="top:22px">$ 4.1</span>
    <span class="txt head" style="top:11px;font-size:26px;color:#fff">Billion MVS<br>to Bodget</span>
  </div>
  <div class="abs stat s2">
    <svg width="294" height="80"><polygon points="90,0 100,0 104,80 94,80" fill="#1689bd"/></svg>
    <span class="big head" style="top:22px">20%</span>
    <span class="txt head" style="top:25px;font-size:17px;line-height:1">Portion of Freight<br><span style="font-size:14px">Rail moved by Vailin MI</span></span>
  </div>
  <div class="abs stat s3">
    <svg width="294" height="80"><polygon points="98,0 294,0 294,80 110,80" fill="#7d8c92"/></svg>
    <span class="big head" style="top:8px;line-height:.9">75%<br><span style="font-size:20px">of all</span></span>
    <span class="txt head" style="top:21px;font-size:15px;line-height:1.2">Fiuished Automabiles<br>Leave MI on Vail</span>
  </div>
  <div class="abs s4a head"><div style="font-size:34px;margin-top:6px;color:var(--navy)">28</div><div style="font-size:15px;line-height:1.15;color:var(--navy)">Freight<br>Railroads in MI</div></div>
  <div class="abs s4b head"><div style="font-size:16px;margin-top:13px;color:var(--navy)">Miles of Travel</div><div style="font-size:36px;margin-top:6px;color:var(--navy)">3,600</div></div>

  <div class="abs safety"></div>
  <div class="abs safety-tag">
    <svg width="180" height="40"><polygon points="0,0 180,0 165,40 0,40" fill="#f4c21f"/><polygon points="0,0 168,0 153,40 0,40" fill="#ef8a1f"/></svg>
    <span class="head">Safety</span>
  </div>
  <div class="abs crossing-art" role="img" aria-label="Illustration of a railroad crossing crossbuck sign with two tracks plate and red signal lights"></div>
  <div class="abs divider" style="left:195px"></div>
  <div class="abs divider" style="left:390px"></div>
  <div class="abs head program" style="left:198px">
    <div class="k1">Crossing Safety</div><div class="k2">Program</div><div class="amt">$ 3m</div>
    <p>Provides Funds For The Elimination Of Hazards At Railway-highway Crossings</p>
  </div>
  <div class="abs head program" style="left:395px">
    <div class="k1">Local Suiface Gvale</div><div class="k2">Crossing</div><div class="amt">$ 3m</div>
    <p>Helps Local To Botter Maintain Local Crossing Surfaces For The Motoring Pulic</p>
  </div>

  <div class="abs front-foot"></div>
  <div class="abs assoc-name">Corvane<br>Transit<br>Assoc</div>
  <div class="abs head foot-line">FREIGHT RAILVOALS =1%<br>Of Total Transportation Budget</div>
</section>

<section class="sheet back">
  <h2 class="abs head back-title">FY 2016-17 MICHIGAN TRANSPORTATION FUND REVENUES AND<br>DISTRIBUTIONS PER Sec. 10, 1951 PA 51</h2>

  <svg class="abs" style="left:0;top:0" width="586" height="665" viewBox="0 0 586 665">
    <defs><marker id="arw" markerWidth="6" markerHeight="6" refX="5" refY="3" orient="auto"><path d="M0,0 L6,3 L0,6 z" fill="#1c7fb4"/></marker></defs>
    <g stroke="#1c7fb4" stroke-width="2.5" fill="none">
      <line x1="292" y1="165" x2="292" y2="420"/>
      <line x1="292" y1="197" x2="266" y2="197" marker-end="url(#arw)"/>
      <line x1="292" y1="248" x2="266" y2="248" marker-end="url(#arw)"/>
      <line x1="292" y1="302" x2="266" y2="302" marker-end="url(#arw)"/>
      <line x1="292" y1="407" x2="266" y2="407" marker-end="url(#arw)"/>
      <line x1="292" y1="275" x2="308" y2="275" marker-end="url(#arw)"/>
      <line x1="292" y1="353" x2="322" y2="353" marker-end="url(#arw)"/>
      <line x1="292" y1="418" x2="314" y2="418" marker-end="url(#arw)"/>
      <line x1="473" y1="432" x2="473" y2="626"/>
      <line x1="473" y1="474" x2="424" y2="474" marker-end="url(#arw)"/>
      <line x1="473" y1="547" x2="424" y2="547" marker-end="url(#arw)"/>
      <line x1="473" y1="626" x2="424" y2="626" marker-end="url(#arw)"/>
      <polyline points="36,330 36,358 52,358" marker-end="url(#arw)"/>
      <polyline points="78,618 78,640 155,640" marker-end="url(#arw)"/>
    </g>
  </svg>

  <div class="flow">
    <div class="box mtf"><b class="h">MICHIGAN TRANSPORTATION FUND (MTF)</b>MTF Revenue = $2,514,863,000<br>Less $21,466,200 to SNR Recreation Improvement Fund<br>Net MTF Revenue = $2,493,396,800</div>

    <div class="box" style="left:35px;top:173px;width:223px;height:47px"><b class="hb">SDOT Local Agency Programs,<br>Planning, Administration, Rail Safety<br>$28,189,000</b></div>
    <div class="box" style="left:35px;top:226px;width:223px;height:46px"><b class="h">To Other State Departments<br>$24,335,000</b>(collection and other support costs)</div>
    <div class="box" style="left:35px;top:279px;width:223px;height:47px"><b class="h">Comprehensive Transportation Fund<br>$220,661,400</b>(10% of net MTF after above deductions)</div>
    <div class="box blue-box" style="left:62px;top:331px;width:168px;height:50px;border-radius:8px">Sales Tax $94,800,000<br>CTF also receives earmark from<br>motor vehicle related sales tax</div>
    <div class="box" style="left:35px;top:385px;width:223px;height:47px"><b class="h">Statutory Grants</b>Local Bridge Fund $ 5,000,000<br>Local Program Fund $33,000,000</div>

    <div class="box grants">
      <b class="hb">STATUTORY GRANTS</b>
      <div class="row"><span>Rail Grade Crossing</span><span class="v">$ 3,000,000</span></div>
      <div class="row"><span>Rail Grade Surface Program</span><span class="v">$ 3,000,000</span></div>
      <div class="row"><span>Local Bridge Fund Debt Service</span><span class="v">$ 2,406,800</span></div>
      <div class="row"><span>3 cent of Gas Tax</span><span class="v">$117,889,500</span></div>
      <div class="row"><span># Local Wetland Mitigation Fund</span><span class="v">$ 4,000,000</span></div>
      <div class="row"><span># Movable Bridge Fund</span><span class="v">$ 10,000,000</span></div>
      <div class="row"><span>½ cent for State Trunkline Bridges</span><span class="v">$ 21,981,600</span></div>
      <div class="row"><span>½ cent for Local Bridges</span><span class="v">$ 21,981,600</span></div>
      <div class="row"><span>STF Debt Reduction</span><span class="v">$ 50,000,000</span></div>
    </div>
    <div class="box sm" style="left:328px;top:332px;width:224px;height:48px;padding-top:2px"><b class="h" style="font-size:8.5px">Transportation Economic Development Fund<br>$40,275,000</b>($36,775,000 + $3,500,000<br>earmarked forTargeted industries)</div>
    <div class="box" style="left:320px;top:385px;width:225px;height:47px;font-size:11px"><b class="h">MTF BALANCE = $1,907,676,900</b><div class="row" style="padding:0 6px"><span>plus 3¢ of Gas Tax (see above)</span><span>$ 117,889,500</span></div><div class="row" style="padding:0 6px"><span>Total to Distribute by Formula</span><span>$2,025,566,400</span></div></div>

    <div class="box county" style="top:441px"><b class="h">COUNTY ROAD COMMISSIONS</b>Total = <b>$813,182,500</b><br>39.1 % of MTF Balance $745,901,700<br>39.1% of 3¢ Gas <b>Tax $ 46,094,800</b><br>Plus $21,186,000 from the Local Program Fund</div>
    <div class="box county" style="top:514px"><b class="h">CITIES AND VILLAGES</b>Total = <b>$453,387,500</b><br>21.8% of MTF Balance $415,873,600<br>21.8% of 3¢ Gas Tax <b>$ 25,699,900</b><br>Plus $11,814,000 from the Local Program Fund</div>
    <div class="box county" style="top:587px;height:75px"><b class="h">STATE TRUNKLINE FUND</b>Total = <b>$863,978,100</b><br>39.1 % of MTF Balance $745,901,700<br>39.1% of 3¢ Gas Tax <b>$ 46,094,800</b><br>Plus $21,981,600 from ½ cent of gas tax for STF bridges<br>and $50,000,000 for STF Debt Reduction</div>

    <div class="box blue-box" style="left:32px;top:483px;width:106px;height:127px;font-size:12px;padding-top:5px">TEDF Transfer<br>$10,400,000<br>House Bill 4440<br>(2016 PA 273)<br>redirected<br>$10.4 million from<br>TEDF Category A<br>program to the STF</div>
  </div>

  <div class="abs back-foot"></div>
  <p class="abs note"><b># Note:</b> This flowchart represents the distribution of MTF revenue as guided by Section 10 of Public Act 51 of 1951, as amended by Public Act 246 of 2016. Public Act 246 established two new earmarks of MTF revenue: $2.0 million for a new Local agency wetland mitigation bank fund, and $5.0 million for a new Movable bridge fund, effective September 22, 2016. For FY 2016-17 the earmarks are twice the fixed statutory amounts because both FY 2015-16 and FY 2016-17 earmarks were appropriated in single year, FY 2016-17, in supplemental appropriation act, Public Act 340 of 2016.</p>
  <div class="abs bureau">Tellis Review Bureau</div>
  <div class="abs byline">Dana R. Whitlow &nbsp;|&nbsp; February 1, 2017</div>
</section>

</body>
</html>
```